Web page for organic mosquito control company in Texas

Looking for a webpage that communicates the three main objectives of the company: Guaranteed effective, Affordable Rates, Organic Solution.
The company specializes in safe organic mosquito control. Service is conducted monthly during the mosquito season. What makes Quillmoor unique is the fact that it does not employ heavy pesticides, expensive equipment purchases and no nozzles misting installed throughout the property. I have some videos that I want to integrate. Please specify what format and codec do want the multi media file in?
Target Market(s)
Mothers 30-55 years of age
Industry/Entity Type
It Company
Number of Pages Required
5+ page
Requirements
Must have
- Predominant space for video on the home page
Nice to have
- Environmental theme without overdoing it.

```html
<!DOCTYPE html>
<html lang="en">
<head>
<meta charset="utf-8">
<title>Quillmoor Mosquito Control System</title>
<link href="https://fonts.googleapis.com/css2?family=Roboto:ital,wght@0,300;0,400;0,500;0,700;1,400&display=swap" rel="stylesheet">
<style>
:root{
  --green:#8cc63f;
  --green-dark:#7db535;
  --ink:#333;
  --muted:#666;
  --dark:#444;
  --footer:#474747;
  --white:#fff;
  --rule:#ddd;
}
*{box-sizing:border-box;margin:0;padding:0}
html,body{width:744px;height:1200px;overflow:hidden;background:var(--white)}
body{font-family:'Roboto',sans-serif;color:var(--ink);position:relative}
.abs{position:absolute}
/* header */
.brand{left:46px;top:10px;width:130px}
.brand-name{font-weight:700;font-size:20px;line-height:21px;color:#4a4a4a;letter-spacing:-.3px}
.brand-tag{font-size:7px;letter-spacing:4px;color:#4a4a4a;margin-top:3px}
.contact-top{left:513px;top:16px;font-size:10px;color:#555;font-style:italic}
.contact-top .row{display:flex;align-items:center;height:24px;gap:8px}
.contact-top .phone{color:var(--green);font-size:13px;font-weight:500}
.dot-ico{width:15px;height:15px;border-radius:50%;background:#e2533f;display:flex;align-items:center;justify-content:center}
/* nav */
.nav{left:0;top:70px;width:744px;height:34px;background:linear-gradient(#94cc48,#80b93a);display:flex;align-items:center;padding-left:63px;gap:0}
.nav a{color:var(--white);font-size:9.5px;text-decoration:none;letter-spacing:.2px;margin-right:23.5px}
/* hero */
.hero{left:0;top:104px;width:744px;height:242px;background:linear-gradient(100deg,#3e5a2c 0%,#6f8a58 30%,#c9cbc4 48%,#9aa98a 65%,#3d5a2b 100%)}
.hero-title{left:0;top:70px;width:744px;text-align:center;color:var(--white);font-size:40px;font-weight:700;letter-spacing:1px;text-shadow:0 2px 4px rgba(0,0,0,.4)}
.hero-sub{left:160px;top:120px;width:424px;text-align:center;color:var(--white);font-size:13px;line-height:16px;text-shadow:0 1px 3px rgba(0,0,0,.6)}
.dots{left:350px;top:214px;display:flex;gap:4px}
.dots span{width:8px;height:8px;border-radius:50%;background:var(--white)}
.dots span:first-child{background:var(--green)}
/* features */
.feature{top:370px;width:180px;text-align:center}
.feature .badge{width:90px;height:90px;margin:0 auto;border-radius:50%;background:var(--green);border:2px solid #d8e8c4;display:flex;align-items:center;justify-content:center}
.feature h3{font-weight:400;font-size:11px;margin-top:16px;color:var(--ink)}
.feature p{font-size:7.5px;line-height:11.5px;color:var(--muted);margin-top:6px;padding:0 12px}
/* welcome */
.welcome{left:0;top:551px;width:744px;height:233px;background:var(--dark)}
.welcome h2{left:47px;top:22px;font-weight:400;font-size:15px;color:var(--green)}
.welcome .copy{left:46px;top:48px;width:316px;font-size:7.8px;line-height:13.2px;color:#e2e2e2;font-weight:300}
.welcome .copy p{margin-bottom:8px}
.btn{left:46px;top:180px;width:86px;height:27px;background:var(--green);color:var(--white);font-size:10px;display:flex;align-items:center;justify-content:center}
.photo{border:2px solid #666}
/* steps */
.section-title{font-weight:400;font-size:14.5px;color:var(--ink)}
.steps-line{left:65px;top:850px;width:1px;height:190px;background:#cfcfcf}
.step{left:47px;width:430px;display:flex;gap:13px}
.step .num{flex:none;width:38px;height:38px;border-radius:50%;background:var(--green);color:var(--white);font-size:17px;font-weight:500;display:flex;align-items:center;justify-content:center;border:2px solid var(--white);box-shadow:0 0 0 1px #d5e6bf}
.step h4{font-weight:400;font-size:9.5px;color:var(--green);margin-top:1px}
.step p{font-size:7px;line-height:11.5px;color:var(--muted);margin-top:4px}
.divider{left:483px;top:810px;width:1px;height:245px;background:var(--rule)}
.testimonial{left:494px;width:198px;display:flex;gap:8px;padding-bottom:8px;border-bottom:1px solid var(--rule)}
.testimonial .thumb{flex:none;width:75px;height:60px;border:1px solid #ccc;display:flex;align-items:center;justify-content:center}
.testimonial h5{font-weight:400;font-size:9.5px;color:var(--green)}
.testimonial p{font-style:italic;font-size:7px;line-height:11.5px;color:var(--muted);margin-top:4px}
.testimonial .more{font-style:italic;font-size:7px;color:var(--ink);margin-top:2px}
/* footer */
.footer{left:0;top:1076px;width:744px;height:124px;background:var(--footer)}
.footer .brand-name{color:var(--white)}
.footer .brand-tag{color:var(--white)}
.footer h6{font-weight:400;font-size:11px;color:var(--green)}
.footer .info{font-size:7.5px;line-height:12.5px;color:#ddd;margin-top:9px}
.footer .info a{color:var(--green);text-decoration:none}
.copyright{left:47px;top:86px;font-size:7.5px;line-height:12.5px;color:#999}
.social{display:flex;flex-direction:column;gap:3px;margin-top:6px}
.social div{display:flex;align-items:center;gap:13px;font-size:7.5px;color:#ddd;height:18px}
.social i{width:18px;height:18px;border-radius:50%;display:block}
</style>
</head>
<body>

<header>
  <div class="abs brand">
    <div class="brand-name">Quillmoor<br>Mosquito</div>
    <div class="brand-tag">Control System</div>
  </div>
  <div class="abs contact-top">
    <div class="row"><span class="dot-ico"><svg width="9" height="9" viewBox="0 0 10 10"><path d="M2 1l2 2-1 1c.5 1.2 1.5 2.2 2.8 2.8l1-1 2 2-1.2 1.2C4.5 9 1 5.5 0.8 2.2z" fill="#fff"/></svg></span>CALL US TODAY: <span class="phone">555-014-2290</span></div>
    <div class="row"><span class="dot-ico"><svg width="9" height="7" viewBox="0 0 9 7"><rect x=".5" y=".5" width="8" height="6" fill="none" stroke="#fff"/><path d="M.5 .5l4 3.2 4-3.2" fill="none" stroke="#fff"/></svg></span>hello@quillmoor-demo.com</div>
  </div>
</header>

<nav class="abs nav">
  <a>HOME</a><a>ABOUT US</a><a>SERVICES</a><a>HOW IT WORKS</a><a>SOLUTION</a><a>PRICING</a><a>FAQ</a><a>TESTIMONIALS</a><a>BLOG</a><a>CONTACT US</a>
</nav>

<section class="abs hero" role="img" aria-label="Video area: technician in orange shirt fogging a garden with organic mosquito mist">
  <h1 class="abs hero-title">MOSQUITO FREEDOM</h1>
  <p class="abs hero-sub">The company specializes in safe organic mosquito control. Service is conducted monthly during the mosquito season.</p>
  <div class="abs dots"><span></span><span></span><span></span><span></span></div>
</section>

<section class="features">
  <div class="abs feature" style="left:59px">
    <div class="badge"><svg width="44" height="40" viewBox="0 0 44 40"><rect x="2" y="16" width="8" height="22" fill="#fff"/><path d="M13 17l8-13c2-3 6-2 5 3l-2 8h14c3 0 4 3 3 5l-4 15c-1 2-2 3-4 3H13z" fill="#fff"/></svg></div>
    <h3>Guaranteed Effective</h3>
    <p>Aliquam molestie, mi et imperdiet euismod, dui purus auctor tellus, et interdum lacus lectus et ante</p>
  </div>
  <div class="abs feature" style="left:282px">
    <div class="badge"><svg width="54" height="40" viewBox="0 0 54 40"><g fill="#fff"><rect x="2" y="3" width="24" height="4"/><rect x="2" y="10" width="24" height="4"/><rect x="2" y="17" width="24" height="4"/><rect x="2" y="24" width="24" height="4"/><rect x="2" y="31" width="24" height="4"/><circle cx="36" cy="22" r="14"/></g><text x="36" y="28" text-anchor="middle" font-family="Roboto,sans-serif" font-weight="700" font-size="17" fill="#8cc63f">$</text></svg></div>
    <h3>Affordable Rates</h3>
    <p>Aliquam molestie, mi et imperdiet euismod, dui purus auctor tellus, et interdum lacus lectus et ante</p>
  </div>
  <div class="abs feature" style="left:506px">
    <div class="badge"><svg width="40" height="48" viewBox="0 0 40 48"><path d="M20 3a16 16 0 0 0-9 29v6h18v-6A16 16 0 0 0 20 3z" fill="none" stroke="#fff" stroke-width="4"/><path d="M20 10c-6 5-6 12 0 17 6-5 6-12 0-17z" fill="#fff"/><rect x="13" y="41" width="14" height="3" fill="#fff"/><rect x="15" y="45" width="10" height="2.5" fill="#fff"/></svg></div>
    <h3>Organic Solution</h3>
    <p>Aliquam molestie, mi et imperdiet euismod, dui purus auctor tellus, et interdum lacus lectus et ante</p>
  </div>
</section>

<section class="abs welcome">
  <h2 class="abs">Welcome to Our Website</h2>
  <div class="abs copy">
    <p>Designed in Texas by Texans, specifically for Texas Mosquitoes, the Quillmoor Mosquito Control System is the first organically-based mosquito control system that eliminates both mosquitoes and the need for automatic mosquito misting systems.</p>
    <p>Our 99.5% organic solution not only minimizes your family's risk to harmful pathogens such as West Nile Virus, Chikungunya, and Eastern Equine Encephalitis, but it also reduces pesticide exposure by 95% compared to nozzle misting systems. Better yet, our customer's report the Quillmoor system is nearly twice as effective as expensive nozzle systems.</p>
  </div>
  <div class="abs btn">READ MORE</div>
  <div class="abs photo" style="left:381px;top:26px;width:150px;height:180px;background:linear-gradient(#7fb04a 0 8%,#3fb3e0 9%,#2aa3d8 70%,#6b5138 71%)" role="img" aria-label="Couple relaxing at the edge of a swimming pool"></div>
  <div class="abs photo" style="left:540px;top:25px;width:158px;height:86px;background:linear-gradient(110deg,#4d6b2f,#9bb07a 55%,#55732f)" role="img" aria-label="Man working in a green garden"></div>
  <div class="abs photo" style="left:540px;top:121px;width:158px;height:86px;background:linear-gradient(#8a8d7a 0 30%,#5d8a2e 31%,#4a7626)" role="img" aria-label="Children playing ball on a backyard lawn"></div>
</section>

<section class="how">
  <h2 class="abs section-title" style="left:47px;top:807px">How the Quillmoor Mosquito Control System Works</h2>
  <div class="abs steps-line"></div>
  <div class="abs step" style="top:841px"><div class="num">1</div><div><h4>Remedying Conducive Conditions to Prevent Egg, Larvae, and Pupae Development..</h4><p>Before a service can commence, a licensed technician will inspect and identify areas to be addressed that are contributing to mosquito harborages at a property.</p></div></div>
  <div class="abs step" style="top:898px"><div class="num">2</div><div><h4>Eradication of adult mosquitoes..</h4><p>Utilizing the most powerful equipment available, technicians direct a pyrethrum-based adulticide deep into mosquito harborages at a velocity of 140 mph to eradicate adult mosquitoes on contact</p></div></div>
  <div class="abs step" style="top:954px"><div class="num">3</div><div><h4>Repelling adult mosquitoes..</h4><p>A mixture of unique essential oils in the Quillmoor solution serve as a strong repellant, preventing mosquitoes. It also acts as a vertical repellant for neighboring mosquitoes trying to establish harborages on the property.</p></div></div>
  <div class="abs step" style="top:1011px"><div class="num">4</div><div><h4>Sterilizing mosquito larvae...</h4><p>When standing water cannot be remedied, the Quillmoor Mosquito Control System utilizes insect-growth-regulators, to treat water receptacles or standing water.</p></div></div>
</section>

<div class="abs divider"></div>

<aside class="testimonials">
  <h2 class="abs section-title" style="left:492px;top:807px">Customer Testimonials</h2>
  <div class="abs testimonial" style="top:835px">
    <div class="thumb" style="background:linear-gradient(120deg,#c9a24a,#e7d7a8 60%,#b28a2e)" role="img" aria-label="Video testimonial from a customer at home"><svg width="22" height="22" viewBox="0 0 22 22"><circle cx="11" cy="11" r="10" fill="rgba(0,0,0,.2)" stroke="#fff" stroke-width="1.5"/><path d="M9 6.5l6 4.5-6 4.5z" fill="#fff"/></svg></div>
    <div><h5>Name goes here</h5><p>Aliquam molestie, mi et imperdiet euismod, dui purus auctor tellus, et interdum lacus lectus et ante..</p><div class="more">Read More</div></div>
  </div>
  <div class="abs testimonial" style="top:915px">
    <div class="thumb" style="background:linear-gradient(120deg,#7d8fa6,#d6d8dc 55%,#3b5f8c)" role="img" aria-label="Video testimonial from a customer"><svg width="22" height="22" viewBox="0 0 22 22"><circle cx="11" cy="11" r="10" fill="rgba(0,0,0,.2)" stroke="#fff" stroke-width="1.5"/><path d="M9 6.5l6 4.5-6 4.5z" fill="#fff"/></svg></div>
    <div><h5>Name goes here</h5><p>Aliquam molestie, mi et imperdiet euismod, dui purus auctor tellus, et interdum lacus lectus et ante..</p><div class="more">Read More</div></div>
  </div>
  <div class="abs testimonial" style="top:995px;border-bottom:none">
    <div class="thumb" style="background:linear-gradient(120deg,#d9b48a,#f1e3cf 55%,#9fb2c4)" role="img" aria-label="Video testimonial from a family"><svg width="22" height="22" viewBox="0 0 22 22"><circle cx="11" cy="11" r="10" fill="rgba(0,0,0,.2)" stroke="#fff" stroke-width="1.5"/><path d="M9 6.5l6 4.5-6 4.5z" fill="#fff"/></svg></div>
    <div><h5>Name goes here</h5><p>Aliquam molestie, mi et imperdiet euismod, dui purus auctor tellus, et interdum lacus lectus et ante..</p><div class="more">Read More</div></div>
  </div>
</aside>

<footer class="abs footer">
  <div class="abs brand" style="left:47px;top:24px">
    <div class="brand-name">Quillmoor<br>Mosquito</div>
    <div class="brand-tag">Control System</div>
  </div>
  <div class="abs copyright">Copyright © 2015. All Right Reserved &nbsp;|&nbsp; Privacy Policy<br>Term of Services</div>
  <div class="abs" style="left:407px;top:19px">
    <h6>Contact Info</h6>
    <div class="info"><span style="color:#fff">Quillmoor Mosquito Control System</span><br>412 Cedar Hollow<br>Lane, Austin, TX 78701<br>Ph: <a>555-014-2290</a><br>Email: <a>hello@quillmoor-demo.com</a></div>
  </div>
  <div class="abs" style="left:572px;top:19px">
    <h6>Connect Us:</h6>
    <div class="social">
      <div><i style="background:#3b5998"></i>Community</div>
      <div><i style="background:#1da1f2"></i>Updates</div>
      <div><i style="background:#d9352b"></i>Videos</div>
      <div><i style="background:#f58220"></i>Feed</div>
    </div>
  </div>
</footer>

</body>
</html>
```